WALKING FOOD TOURISM BUSINESS. REQUEST FOR DIGITAL BROCHURE

Our business is a walking food tourism business in and around Melbourne's central city. We are needing a e-digital brochure - to be solely used as email' marketing content, not print. Therefore PDF size needs to be appropriate/suitable. Please see attached written content required for the brochure - together with our logo. For images, I am happy for designer to use our website content (www.gullyandfork.com). OR any other appropriate and creative 'foodie' or Melbourne image suitable. Many thanks:)

Target Market(s)

Premium brand travellers or local adventurous Australians.

Requirements
Must have
• Quality font and images
Nice to have
• Quality Melbourne and food images. See website - gullyandfork.com
Should not have
• Too much colour. Brand is black and white, sophisticated, premium product.

```html
<!DOCTYPE html>
<html lang="en">
<head>
<meta charset="utf-8">
<title>Gully and Fork – Walking Food Tours Brochure</title>
<link rel="stylesheet" href="https://fonts.googleapis.com/css2?family=Roboto+Condensed:ital,wght@0,400;0,700;1,700&display=swap">
<style>
:root{
  --ink:#1e1e1e;
  --slate:#3e4a54;
  --slate-deep:#26313a;
  --label:#2b3640;
  --paper:#ffffff;
  --rule:#9aa3aa;
  --page-bg:#ffffff;
  --on-dark:#f2f4f5;
}
*{box-sizing:border-box;margin:0;padding:0}
html,body{width:1200px;height:1000px;overflow:hidden;background:var(--page-bg)}
body{position:relative;font-family:"Roboto Condensed",Arial Narrow,sans-serif;color:var(--ink)}
.brochure{
  position:absolute;left:429px;top:11px;width:605px;height:1730px;
  transform:scale(.565);transform-origin:0 0;
  background:var(--paper);border:1px solid var(--rule);overflow:hidden;
}
.abs{position:absolute}
.photo{position:absolute}
.hero{left:0;top:0;width:605px;height:303px;
  background:linear-gradient(180deg,#c9c3bb 0%,#6e6558 30%,#3f4a3a 62%,#5f8a36 80%,#7fa548 100%)}
.hero-band{left:0;top:78px;width:605px;height:147px;background:rgba(30,40,50,.62)}
.brand-name{left:0;top:128px;width:605px;text-align:center;color:#fff;font-size:34px;font-weight:400;letter-spacing:1px;
  display:flex;justify-content:center;align-items:center;gap:12px}
.brand-mark{width:12px;height:12px;border:2px solid #fff}
.label{position:absolute;background:var(--label);color:#fff;font-weight:700;font-size:12px;padding:1px 6px;line-height:15px}
.label-rule{position:absolute;height:3px;width:44px;background:var(--label)}
.body{font-size:11.6px;line-height:14.9px;text-align:justify}
.tour-title{position:absolute;font-weight:700;font-size:12.5px}
.tour-meta{position:absolute;font-weight:700;font-style:italic;font-size:10.5px}
.panel{position:absolute;background:var(--slate);color:var(--on-dark)}
.panel .tour-title,.panel .tour-meta{position:static}
.street-panel{left:30px;top:684px;width:200px;height:321px;padding:8px 6px}
.street-panel .body{margin:10px 10px 0 10px}
.story-text{left:310px;top:1060px;width:258px}
.story-spacer{float:left;width:137px;height:192px}
.evening-text{left:30px;top:1358px;width:260px}
.plate{float:left;width:150px;height:150px;border-radius:50%;shape-outside:circle(50%);margin:4px 6px 0 6px;
  background:radial-gradient(circle,#7a1e2a 0%,#4a1218 40%,#1b1b1b 62%)}
.private-panel{left:302px;top:1312px;width:272px;height:251px;padding:7px 9px}
.private-panel .tour-title{display:block}
.private-panel .rule{width:44px;height:3px;background:#fff;margin:5px 0 6px}
.private-panel .body{font-size:11.3px;line-height:14px}
.footer{left:0;top:1588px;width:605px;height:142px;background:var(--slate)}
.footer-strip{left:0;top:1713px;width:605px;height:17px;background:var(--slate-deep)}
.pill{position:absolute;background:var(--slate-deep);color:#fff;font-weight:700;font-size:12px;padding:2px 12px;border-radius:10px;line-height:14px}
.contact{position:absolute;color:#fff;font-size:12px;display:flex;align-items:center;gap:8px}
.icon-box{width:18px;height:18px;border:1.3px solid #fff;border-radius:4px;display:flex;align-items:center;justify-content:center}
.policy{position:absolute;left:50px;color:#fff;font-size:11.5px}
.policy b{font-weight:700}
</style>
</head>
<body>
<main class="brochure">
  <div class="photo hero" role="img" aria-label="Tree-lined park path leading to a domed heritage exhibition building"></div>
  <div class="abs hero-band"></div>
  <div class="abs brand-name"><span class="brand-mark"></span>Gully and Fork</div>

  <span class="label" style="left:30px;top:320px">About Us</span>
  <span class="label-rule" style="left:35px;top:341px"></span>
  <p class="abs body" style="left:38px;top:356px;width:322px">We provide experiential adventure for visitors and locals alike - all through the ‘lens’ of exceptional food. Our tour experiences capture the essence of Melbourne, its people and diverse history - stopping to sip, savour and delight in Melbourne’s foodie hot spots &amp; indulging in their signature tastes.</p>
  <div class="photo" style="left:385px;top:349px;width:189px;height:127px;background:linear-gradient(135deg,#8d8a84,#4b4640 55%,#7a2b2b)" role="img" aria-label="Tour group gathered in a busy city laneway"></div>

  <span class="label" style="left:30px;top:443px">Our Experiences</span>
  <span class="label-rule" style="left:35px;top:464px"></span>
  <h2 class="tour-title" style="left:35px;top:477px">Foodies Bucket List Tour</h2>
  <p class="tour-meta" style="left:35px;top:494px">3.5 hours / A$159 Adult / A$119 Child / Up to 8 guests</p>
  <div class="photo" style="left:30px;top:520px;width:329px;height:145px;background:linear-gradient(120deg,#3a2a1e,#b8905a 45%,#6b7a3a 70%,#d9d3c8)" role="img" aria-label="Bowl of noodles topped with fresh herbs"></div>
  <p class="abs body" style="left:385px;top:518px;width:190px">Think you’re a foodie? Are you torn by delicious culinary choices and have a fear of missing out on the true Melbourne foodie experience? If your answers are ‘yes’, then our ‘Bucket List’ adventure is for you.<br>When time is of the essence, our ‘Bucket List Tour’ will ‘wow’ your senses - while tasting and strolling your way through Melbourne’s exploding culinary epicentre.</p>

  <section class="panel street-panel">
    <h2 class="tour-title">Street Eats Tour</h2>
    <p class="tour-meta" style="margin-top:4px;line-height:15px">3 hours / A$110 Adult / A$70.00 Child /<br>Up to 10 guests</p>
    <p class="body">Hungry? Then why not broaden your palette and TAKE IT TO THE STREETS - Melbourne style. Our Street Eats Tour is ideal for locals and visitors, keen to wander, explore &amp; taste Melbourne’s Asian ‘street food’ scene. Taste your way in and around Melbourne – slurping up Thai noodles, devouring Shanghai Dumplings, Korean bites, Japanese treats and more – whilst taking in mystical immigrant stories - from the Chinese arrival, the Vietnamese and later, the sub-continent. The perfect experience to capture some of Melbourne’s best, hidden treasures.</p>
  </section>
  <div class="photo" style="left:231px;top:684px;width:344px;height:169px;background:linear-gradient(135deg,#2d241c,#a0642a 45%,#c98b45 70%,#e4d8c4)" role="img" aria-label="Box of crispy fried chicken pieces"></div>
  <div class="photo" style="left:231px;top:861px;width:171px;height:144px;background:linear-gradient(135deg,#5a4a38,#e8e2d6 50%,#6a5a8a)" role="img" aria-label="Steamed bao buns with slaw filling"></div>
  <div class="photo" style="left:410px;top:861px;width:163px;height:144px;background:linear-gradient(160deg,#3d5a7a,#2b2f38 55%,#8a7a5a)" role="img" aria-label="Group of tour guests posing in a lit arcade"></div>

  <h2 class="tour-title" style="left:35px;top:1026px">The Story of Melbourne</h2>
  <p class="tour-meta" style="left:35px;top:1042px">2.5 hours / A$89 Adult / A$49 Child / Up to 12 guests</p>
  <div class="photo" style="left:30px;top:1060px;width:187px;height:233px;background:linear-gradient(170deg,#3d6ab5,#a9b07a 45%,#6b6a40)" role="img" aria-label="Gothic cathedral spire against blue sky"></div>
  <div class="photo" style="left:220px;top:1060px;width:223px;height:185px;background:linear-gradient(180deg,#7a9ccf,#c9a56a 45%,#3a4f6a 60%,#8aa0b8)" role="img" aria-label="City skyline reflected in the river at dusk"></div>
  <div class="photo" style="left:148px;top:1130px;width:142px;height:163px;background:linear-gradient(160deg,#9a8a78,#5a4a3e 50%,#2e2a28)" role="img" aria-label="Guests tasting at a distillery bar"></div>
  <div class="abs story-text body"><span class="story-spacer"></span>From the Yarra River to Iconic Laneways, Historic Precincts, Theatres &amp; Cathedrals - discover the character, culture &amp; community of our magnificent city, that is MELBOURNE. Walk with us on tour, as we share stories about Melbourne’s past and present. Along your journey you’ll take in the very fabric of Melbourne. From the early beginnings – through to today, soaking in why Melbourne continues to be one of the greatest multi-cultural cities in the world.</div>

  <h2 class="tour-title" style="left:35px;top:1320px">Evening Palate &amp; Pairing</h2>
  <p class="tour-meta" style="left:35px;top:1337px">3 hours / A$199 Adult / A$159 Child / Up to 8 guests</p>
  <span class="abs" style="left:235px;top:1352px;width:55px;height:3px;background:var(--label)"></span>
  <div class="abs evening-text body"><span class="plate" role="img" aria-label="Plated dessert with berry sauce on a black plate"></span>Enjoy your evening in one of Melbourne most vibrant, mouth-watering, delectable foodie precincts. You’ll be ‘wowed’ by Melbourne’s charm and hospitality as you experience signature tastes from some of our best restaurants – pairing flavours and textures at each venue – and hearing the stories that transformed Melbourne into the marvellous ‘food capital’ city it is today.</div>

  <section class="panel private-panel">
    <h2 class="tour-title">Private Experiences</h2>
    <p class="tour-meta" style="margin-top:4px">Up to 8 hours / Tailored itineraries</p>
    <div class="rule"></div>
    <p class="body">Our private tours are ideal for the ultimate fun ‘group adventure’. Share and experience the cultural delights of Melbourne with good friends – perhaps a team building event, a family reunion, a special birthday or wedding party. All with your very own personal tour host. Choose from one of our Gully and Fork Experiences – with the option to customise the tour length, start time and tour distance covered. OR tailor your own experience to suit your interest, theme, community and corporate groups. Either way, your PRIVATE EXPERIENCE will be created with you in mind.</p>
    <p class="body" style="margin-top:4px;text-align:left">Enquiries: <i>info@gullyandfork.com</i></p>
  </section>

  <footer>
    <div class="abs footer"></div>
    <div class="abs footer-strip"></div>
    <span class="pill" style="left:30px;top:1598px">For Booking Schedule &amp; Enquiry</span>
    <div class="contact" style="left:52px;top:1623px">
      <span class="icon-box"><svg width="12" height="12" viewBox="0 0 24 24"><path d="M6.6 10.8a15.1 15.1 0 0 0 6.6 6.6l2.2-2.2a1 1 0 0 1 1-.25 11.4 11.4 0 0 0 3.6.57 1 1 0 0 1 1 1V20a1 1 0 0 1-1 1A17 17 0 0 1 3 4a1 1 0 0 1 1-1h3.5a1 1 0 0 1 1 1 11.4 11.4 0 0 0 .57 3.6 1 1 0 0 1-.25 1z" fill="none" stroke="#fff" stroke-width="2"/></svg></span>
      +61 400 118 246
    </div>
    <span class="pill" style="left:300px;top:1598px">Socials</span>
    <div class="contact" style="left:312px;top:1623px"><span class="icon-box" style="border-radius:50%"></span>gullyandfork.eats</div>
    <div class="contact" style="left:460px;top:1623px"><span class="icon-box"></span>GullyAndFork.Tours</div>
    <span class="pill" style="left:30px;top:1650px">Cancellation &amp; Amendments</span>
    <p class="policy" style="top:1675px"><b>100% REFUND</b> for cancellations outside 24 hours of the tour departure time</p>
    <p class="policy" style="top:1693px"><b>NO REFUND</b> for cancellations made within 24 hours of the tour departure time</p>
  </footer>
</main>
</body>
</html>
```